BWN: Schedule an appointment online

Hi,
Looking for an 8.5x11 flyer
Needs to be in several formats and different resolutions, png, jpeg, pdf, vector
The objective is to let our patients know we are now offering online scheduling through our website. Patients can now schedule an appointment online.
I've added two of our previous flyers through pixel harbor as examples.
We want simple and to the point, emphasis on Scheduling an appointment online.
Please include our website, phone number and addresses of our locations (see example flyers)
Thank you,
Marcus

```html
<!DOCTYPE html>
<html lang="en">
<head>
<meta charset="utf-8">
<title>BWN Foot &amp; Ankle – Schedule Online</title>
<link href="https://fonts.googleapis.com/css2?family=Poppins:wght@400;500;600;700;800&display=swap" rel="stylesheet">
<style>
  :root{
    --backdrop:#8c8c8c;
    --paper:#ffffff;
    --charcoal:#2e2e2e;
    --teal:#4dbf9f;
    --teal-dark:#3a9a80;
    --orange:#ec6b35;
    --ink:#2b2b2b;
    --white:#ffffff;
  }
  *{margin:0;padding:0;box-sizing:border-box}
  html,body{width:1200px;height:1200px;overflow:hidden}
  body{background:var(--backdrop);font-family:"Poppins",sans-serif;position:relative}
  .flyer{position:absolute;left:150px;top:17px;width:900px;height:1165px;background:var(--paper);overflow:hidden}

  .brand{position:absolute;left:290px;top:30px;width:352px;height:100px}
  .brand-dot{position:absolute;left:0;top:22px;width:56px;height:56px;border-radius:50%;background:var(--teal)}
  .brand-text{position:absolute;right:0;top:0;color:var(--orange);font-weight:700;text-align:right}
  .brand-name{font-size:34px;line-height:36px;letter-spacing:.3px}
  .brand-url{font-size:16px;line-height:20px;letter-spacing:.3px}

  .hero-photo{position:absolute;left:0;top:129px;width:900px;height:358px;
    background:linear-gradient(180deg,#ffffff 0%,#eef2f5 22%,#dfe6ec 50%,#d9a894 75%,#c98f7c 100%)}
  .dark-band{position:absolute;left:0;top:486px;width:900px;height:530px;background:var(--charcoal)}
  .dark-corner{position:absolute;left:640px;top:1000px;width:260px;height:165px;background:var(--charcoal)}

  .banner-tab{position:absolute;left:105px;top:443px;width:692px;height:60px;background:var(--teal-dark);border-radius:30px 30px 0 0}
  .banner{position:absolute;left:166px;top:443px;width:569px;height:282px;background:var(--teal);border-radius:0 0 26px 26px;
    box-shadow:0 10px 22px rgba(0,0,0,.35);color:var(--white);font-weight:800;line-height:1}
  .banner .line{position:absolute;left:0;right:0;text-align:center;white-space:nowrap}
  .banner .l1{top:32px;font-size:60px;letter-spacing:-1px}
  .banner .l2{top:82px;font-size:64px;letter-spacing:-1.5px}
  .banner .l3{top:131px;font-size:138px;letter-spacing:-3px}

  .feature{position:absolute;top:768px;display:flex;align-items:center;gap:12px;color:var(--white);font-size:19px;line-height:23px}
  .feature.f1{left:93px}
  .feature.f2{left:359px}
  .feature.f3{left:632px}
  .divider{position:absolute;top:770px;width:1px;height:48px;background:#3c3c3c}

  .contact-icon{position:absolute;left:89px;top:876px}
  .contact-label{position:absolute;left:183px;top:870px;font-size:27px;font-weight:600;color:var(--white);line-height:34px;letter-spacing:.3px}
  .contact-phone{position:absolute;left:181px;top:901px;font-size:54px;font-weight:700;color:var(--white);line-height:60px}

  .web-pill{position:absolute;left:173px;top:996px;width:336px;height:36px;border-radius:18px;background:var(--orange);
    color:var(--white);font-size:23px;display:flex;align-items:center;justify-content:center;gap:8px}

  .office{position:absolute;top:1050px;color:var(--ink);font-size:13.5px;line-height:15px}
  .office.o1{left:46px}
  .office.o2{left:241px}
  .office.o3{left:459px}
  .office h3{color:var(--orange);font-size:18px;font-weight:600;display:flex;align-items:center;gap:4px;margin-bottom:4px;line-height:22px}
  .office p{padding-left:17px}
  .office-rule{position:absolute;top:1052px;height:68px;border-left:2px dotted var(--orange)}

  .phone-photo{position:absolute;left:642px;top:846px;width:136px;height:277px;border-radius:20px;
    background:linear-gradient(180deg,#4a4a4a 0%,#262626 40%,#1d1d1d 100%);border:3px solid #bfb6ae}
</style>
</head>
<body>
<main class="flyer">
  <div class="hero-photo" role="img" aria-label="Podiatrist in white coat and gloves examining a patient's bare foot"></div>

  <header class="brand">
    <span class="brand-dot"></span>
    <div class="brand-text">
      <div class="brand-name">BWN</div>
      <div class="brand-name">FOOT &amp; ANKLE</div>
      <div class="brand-url">STEPWELLCLINIC.COM</div>
    </div>
  </header>

  <div class="dark-band"></div>
  <div class="dark-corner"></div>
  <div class="banner-tab"></div>
  <section class="banner">
    <div class="line l1">SCHEDULING AN</div>
    <div class="line l2">APPOINTMENT</div>
    <div class="line l3">ONLINE</div>
  </section>

  <div class="feature f1">
    <svg width="40" height="40" viewBox="0 0 40 40"><circle cx="20" cy="20" r="18" fill="none" stroke="#fff" stroke-width="2"/><circle cx="20" cy="20" r="13" fill="none" stroke="#fff" stroke-width="1.5"/><path d="M13 20l5 5 9-10" fill="none" stroke="#fff" stroke-width="2.5"/></svg>
    <span>Faster<br>Checkout times</span>
  </div>
  <div class="divider" style="left:323px"></div>
  <div class="feature f2">
    <svg width="40" height="40" viewBox="0 0 40 40"><circle cx="20" cy="20" r="18" fill="none" stroke="#fff" stroke-width="2"/><circle cx="20" cy="20" r="13" fill="none" stroke="#fff" stroke-width="1.5"/><path d="M13 20l5 5 9-10" fill="none" stroke="#fff" stroke-width="2.5"/></svg>
    <span>Greater security<br>with card</span>
  </div>
  <div class="divider" style="left:600px"></div>
  <div class="feature f3">
    <svg width="40" height="40" viewBox="0 0 40 40"><circle cx="20" cy="20" r="18" fill="none" stroke="#fff" stroke-width="2"/><circle cx="20" cy="20" r="13" fill="none" stroke="#fff" stroke-width="1.5"/><path d="M13 20l5 5 9-10" fill="none" stroke="#fff" stroke-width="2.5"/></svg>
    <span>Contactless<br>payments</span>
  </div>

  <svg class="contact-icon" width="82" height="82" viewBox="0 0 82 82"><circle cx="41" cy="41" r="39" fill="none" stroke="#ec6b35" stroke-width="2"/><path d="M30 24c3-2 5 0 7 4 2 4 1 6-1 7-1 1-1 3 1 6s5 6 7 6 2-1 3-2c2-2 4-1 7 1 4 3 4 5 2 7-3 3-7 4-13 0-6-4-12-11-14-17-2-6-1-10 1-12z" fill="none" stroke="#ec6b35" stroke-width="2"/></svg>
  <div class="contact-label">CONTACT US TODAY!</div>
  <div class="contact-phone">(555)214-0370</div>

  <div class="web-pill">
    <svg width="22" height="22" viewBox="0 0 22 22" fill="none" stroke="#fff" stroke-width="1.4"><circle cx="11" cy="11" r="9"/><ellipse cx="11" cy="11" rx="4" ry="9"/><path d="M2 11h18M4 6h14M4 16h14"/></svg>
    www.stepwellclinic.com
  </div>

  <div class="office o1">
    <h3><svg width="13" height="16" viewBox="0 0 13 16"><path d="M6.5 15S1 9 1 6a5.5 5.5 0 0111 0c0 3-5.5 9-5.5 9z" fill="none" stroke="#4dbf9f" stroke-width="2"/><circle cx="6.5" cy="6" r="1.8" fill="#4dbf9f"/></svg>Northgate Office</h3>
    <p>48 Linden Park Dr.<br>Ste. 170<br>Northgate, MD 20990</p>
  </div>
  <div class="office-rule" style="left:230px"></div>
  <div class="office o2">
    <h3><svg width="13" height="16" viewBox="0 0 13 16"><path d="M6.5 15S1 9 1 6a5.5 5.5 0 0111 0c0 3-5.5 9-5.5 9z" fill="none" stroke="#4dbf9f" stroke-width="2"/><circle cx="6.5" cy="6" r="1.8" fill="#4dbf9f"/></svg>Riverside Office</h3>
    <p>72 Willow Bend Rd.<br>Riverside, WV 24990</p>
  </div>
  <div class="office-rule" style="left:447px"></div>
  <div class="office o3">
    <h3><svg width="13" height="16" viewBox="0 0 13 16"><path d="M6.5 15S1 9 1 6a5.5 5.5 0 0111 0c0 3-5.5 9-5.5 9z" fill="none" stroke="#4dbf9f" stroke-width="2"/><circle cx="6.5" cy="6" r="1.8" fill="#4dbf9f"/></svg>Hillcrest Office</h3>
    <p>915 Maple Crest Blvd.<br>Ste. 201<br>Hillcrest, MD 20995</p>
  </div>

  <div class="phone-photo" role="img" aria-label="Hand holding a smartphone showing the online appointment booking page"></div>
</main>
</body>
</html>
```